Business Card Design Project Bright Way

Simple and clean business card,

Logo and fond added in attachment

Data need to be changable:
Lien Varmeko
Customer Service Specialist

Bright Way - lien.varmeko@brightway-mail.be - Mob: +32471538046 - www.brightway-mail.be

Target Market(s)

Small businesses

Industry/Entity Type

Business

Requirements
Nice to have
• QR-code

```html
<!DOCTYPE html>
<html lang="en">
<head>
<meta charset="utf-8">
<title>Bright Way – Business Card</title>
<link rel="stylesheet" href="https://fonts.googleapis.com/css2?family=Open+Sans:wght@400;700&display=swap">
<style>
  :root {
    --brand-blue: #00a9ea;
    --brand-green: #8cc63f;
    --ink: #333333;
    --card: #ffffff;
    --backdrop: #4a88aa;
  }
  * { margin: 0; padding: 0; box-sizing: border-box; }
  html, body {
    width: 1200px;
    height: 806px;
    overflow: hidden;
    background: var(--backdrop);
    font-family: "Open Sans", Arial, sans-serif;
  }
  .card {
    position: absolute;
    left: 50px;
    top: 70px;
    width: 1100px;
    height: 665px;
    background: var(--card);
    overflow: hidden;
  }
  .brand {
    position: absolute;
    left: 59px;
    top: 92px;
    display: flex;
    align-items: center;
    gap: 30px;
  }
  .brand-mark {
    width: 150px;
    height: 150px;
    background: var(--brand-blue);
    border-radius: 22px;
  }
  .brand-name {
    font-size: 118px;
    font-weight: 400;
    color: var(--brand-green);
    line-height: 1;
    letter-spacing: -1px;
    white-space: nowrap;
  }
  .person {
    position: absolute;
    left: 603px;
    top: 297px;
  }
  .person-name {
    font-size: 34px;
    font-weight: 700;
    color: var(--brand-blue);
    line-height: 1.2;
  }
  .person-role {
    font-size: 23px;
    color: var(--ink);
    margin-top: 4px;
  }
  .contacts {
    position: absolute;
    left: 603px;
    top: 417px;
    list-style: none;
  }
  .contact {
    display: flex;
    align-items: center;
    height: 46px;
    font-size: 24px;
    color: var(--ink);
  }
  .contact-icon {
    width: 28px;
    height: 28px;
    margin-right: 28px;
    fill: var(--brand-blue);
    flex-shrink: 0;
  }
  .footer-bands {
    position: absolute;
    left: 0;
    bottom: 0;
    width: 1100px;
    height: 45px;
  }
</style>
</head>
<body>
  <main class="card">
    <div class="brand">
      <div class="brand-mark"></div>
      <div class="brand-name">Bright Way</div>
    </div>

    <section class="person">
      <h1 class="person-name">Lien Varmeko</h1>
      <p class="person-role">Customer Service Specialist</p>
    </section>

    <ul class="contacts">
      <li class="contact">
        <svg class="contact-icon" viewBox="0 0 28 28" aria-hidden="true">
          <path d="M3 9c0-3 5-5 11-5s11 2 11 5v2h-6V9c-1-1-3-1.5-5-1.5S10 8 9 9v2H3z"/>
          <path d="M8 12h12l4 10H4z"/>
        </svg>
        <span>+32471538046</span>
      </li>
      <li class="contact">
        <svg class="contact-icon" viewBox="0 0 28 28" aria-hidden="true">
          <path d="M2 6h24v16H2z M3 7l11 9 11-9v-0.5H3z" fill-rule="evenodd"/>
          <path d="M2 6l12 10 12-10v2L14 18 2 8z" fill="#fff"/>
        </svg>
        <span>lien.varmeko@brightway-mail.be</span>
      </li>
      <li class="contact">
        <svg class="contact-icon" viewBox="0 0 28 28" aria-hidden="true">
          <circle cx="14" cy="14" r="12"/>
          <g fill="none" stroke="#fff" stroke-width="1.6">
            <ellipse cx="14" cy="14" rx="5" ry="12"/>
            <path d="M14 2v24M2 14h24M4 8h20M4 20h20"/>
          </g>
        </svg>
        <span>www.brightway-mail.be</span>
      </li>
    </ul>

    <svg class="footer-bands" viewBox="0 0 1100 45" preserveAspectRatio="none" aria-hidden="true">
      <polygon points="0,0 554,0 590,45 0,45" fill="var(--brand-blue)"/>
      <polygon points="568,17 1100,17 1100,45 590,45" fill="var(--brand-green)"/>
    </svg>
  </main>
</body>
</html>
```